HomeBridle business card and stationary design

We are looking for a simple yet elegant design for our mortgage company business card and stationary.

The card should include:
Name (Derek Walsh)
Title (CEO)
Phone Number (614-208-3917)
Address (48 Birchfield Court, Suite 314, Marlow, OH 43952)
Email (email@homebridle-example.com)
"NMLS" i.e. (NMLS 61947)
"Company NMLS" (Company NMLS 472815)

See above

```html
<!DOCTYPE html>
<html lang="en">
<head>
<meta charset="utf-8">
<title>HomeBridle Business Card</title>
<link rel="stylesheet" href="https://fonts.googleapis.com/css2?family=Source+Sans+3:wght@400;600;700&display=swap">
<style>
  :root {
    --bg: #d9d9d9;
    --navy: #1b2733;
    --navy-light: #2c3a47;
    --navy-band: #141d26;
    --sky: #2fa9e6;
    --sky-pale: #a9d8f3;
    --white: #ffffff;
    --ink-soft: #dfe6ec;
  }
  * { margin: 0; padding: 0; box-sizing: border-box; }
  html, body { width: 1200px; height: 675px; overflow: hidden; }
  body {
    background: var(--bg);
    font-family: "Source Sans 3", "Segoe UI", sans-serif;
    display: flex;
    align-items: center;
    justify-content: center;
    gap: 60px;
  }
  .card {
    position: relative;
    width: 520px;
    height: 297px;
    border-radius: 14px;
    overflow: hidden;
    box-shadow: 0 8px 24px rgba(0,0,0,0.18);
  }
  .card-art { position: absolute; inset: 0; width: 100%; height: 100%; }

  /* Front */
  .card-front { background: linear-gradient(135deg, var(--navy-light), var(--navy)); }
  .front-wordmark {
    position: absolute;
    top: 96px;
    left: 0; right: 0;
    text-align: center;
    font-weight: 600;
    font-size: 56px;
    letter-spacing: 1px;
    color: var(--white);
  }

  /* Back */
  .card-back { background: var(--white); }
  .back-wordmark {
    position: absolute;
    top: 46px;
    right: 40px;
    font-weight: 600;
    font-size: 40px;
    color: var(--navy);
  }
  .person {
    position: absolute;
    right: 40px;
    bottom: 44px;
    text-align: right;
  }
  .person-name {
    font-weight: 700;
    font-size: 20px;
    color: var(--sky);
    text-transform: uppercase;
    letter-spacing: 0.5px;
  }
  .person-title {
    font-weight: 700;
    font-size: 11px;
    color: var(--navy);
    margin-top: 2px;
  }
  .contact-list {
    position: absolute;
    left: 28px;
    bottom: 26px;
    list-style: none;
    color: var(--ink-soft);
    font-size: 13px;
    line-height: 1.55;
  }
  .contact-list li::before {
    content: "";
    display: inline-block;
    width: 4px; height: 4px;
    border-radius: 50%;
    background: var(--ink-soft);
    margin-right: 8px;
    vertical-align: middle;
  }
  .contact-list .indent { padding-left: 12px; }
  .contact-list .indent::before { display: none; }
</style>
</head>
<body>
  <section class="card card-front" aria-label="Business card front">
    <svg class="card-art" viewBox="0 0 520 297" aria-hidden="true">
      <polygon points="0,205 300,205 520,297 0,297" fill="var(--navy-band)" opacity="0.55"/>
    </svg>
    <div class="front-wordmark">HomeBridle</div>
  </section>

  <section class="card card-back" aria-label="Business card back">
    <svg class="card-art" viewBox="0 0 520 297" aria-hidden="true">
      <polygon points="0,50 270,118 350,297 330,297 258,130 0,64" fill="var(--sky-pale)"/>
      <polygon points="0,64 258,130 330,297 0,297" fill="var(--navy)"/>
    </svg>
    <div class="back-wordmark">HomeBridle</div>
    <ul class="contact-list">
      <li>48 Birchfield Court,</li>
      <li class="indent">Suite 314, Marlow, OH 43952</li>
      <li>614-208-3917</li>
      <li>email@homebridle-example.com</li>
      <li>NMLS 61947</li>
      <li>Company NMLS 472815</li>
    </ul>
    <div class="person">
      <div class="person-name">Derek Walsh</div>
      <div class="person-title">CEO</div>
    </div>
  </section>
</body>
</html>
```